Pool Screen Enclosure Building a Career Boot Camp!

Looking to Host a Boot Camp for people looking for a career or looking to change careers. We Design, Manufacture and Install Custom Pool Screen Enclosures. We have a training program to allow Non Experienced motivated people the chance at a great career that will provide a great living for them and their family. This will be a paid boot camp, week long, we provide all the initial training for them to make a transition into our business. This will be 5 days of training with a guaranteed job to start the following Monday.... This is good for both someone with no construction experience or someone with construction experience that wants to upgrade their current job.
Paid Boot Camp
transition to a full time job with great pay
Benefits include Health Insurance, Dental and Vision, 401K, we provide the tools and training.

```html
<!DOCTYPE html>
<html lang="en">
<head>
<meta charset="utf-8">
<title>Boot Camp Flyer</title>
<link href="https://fonts.googleapis.com/css2?family=Montserrat:wght@400;500;600;700;800&display=swap" rel="stylesheet">
<style>
:root{
  --stage:#333333;
  --paper:#ffffff;
  --green-dark:#23772f;
  --green:#3aa440;
  --green-light:#5cc04a;
  --yellow:#ffe438;
  --yellow-deep:#f7d21e;
  --ink:#2b2b36;
  --body:#3c3c46;
  --photo-sky:#8b98a6;
  --photo-water:#3f6f72;
}
*{margin:0;padding:0;box-sizing:border-box}
html,body{width:1200px;height:1000px;overflow:hidden;background:var(--stage);font-family:'Montserrat',sans-serif}
.flyer{position:absolute;left:280px;top:86px;width:640px;height:828px;background:var(--paper);overflow:hidden}
.art{position:absolute;left:0;top:0}
.brand{position:absolute;left:36px;top:40px;display:flex;align-items:center;gap:10px}
.brand-mark{width:26px;height:26px;background:var(--ink)}
.brand-name{font-weight:700;font-size:21px;color:var(--ink)}
.brand-tag{position:absolute;left:72px;top:70px;font-size:10px;font-weight:500;color:var(--body)}
.headline{position:absolute;left:36px;top:138px;color:#fff;font-weight:800;line-height:1.05}
.headline .l1{font-size:29px}
.headline .l2{font-size:30px;color:var(--yellow);padding-left:30px}
.headline .l3{font-size:26px;margin-top:16px}
.headline .l4{font-size:26px}
.headline .sub{font-size:15px;color:var(--yellow);font-weight:700;padding-left:28px;margin-top:1px}
.headline small{font-size:15px;color:var(--yellow);font-weight:700}
.services{position:absolute;left:0;width:640px;top:502px;text-align:center;font-size:25px;font-weight:700;color:var(--ink);line-height:1.15}
.col{position:absolute;top:572px;font-size:11px;color:var(--body);line-height:1.4}
.col.left{left:36px;width:266px}
.col.right{left:360px;width:236px}
.divider{position:absolute;left:330px;top:572px;width:2px;height:140px;background:var(--green-dark)}
.item{display:flex;gap:10px;margin-bottom:10px}
.item svg{flex:none;margin-top:1px}
.camp{position:absolute;left:36px;top:705px;width:250px}
.camp h2{font-size:20px;font-weight:700;color:var(--ink);margin-bottom:8px}
.camp .item{font-size:11px;font-weight:600;color:var(--ink);line-height:1.4;margin-bottom:8px}
.contact{position:absolute;left:336px;top:730px;color:#fff}
.contact .row{display:flex;align-items:center;gap:14px;margin-bottom:5px}
.contact .phone{font-size:22px;font-weight:700}
.contact .txt{font-size:15px;font-weight:500;line-height:1.35}
.ico{width:20px;height:20px;border-radius:50%;background:var(--yellow);display:flex;align-items:center;justify-content:center;flex:none}
</style>
</head>
<body>
<div class="flyer">
  <svg class="art" width="640" height="828" viewBox="0 0 640 828">
    <defs>
      <linearGradient id="greenBand" x1="0" y1="0" x2="1" y2="0">
        <stop offset="0" stop-color="#23772f"/>
        <stop offset="1" stop-color="#5cc04a"/>
      </linearGradient>
      <linearGradient id="poolScene" x1="0" y1="0" x2="0" y2="1">
        <stop offset="0" stop-color="#a9b4bf"/>
        <stop offset=".6" stop-color="#8b98a6"/>
        <stop offset="1" stop-color="#3f6f72"/>
      </linearGradient>
      <linearGradient id="footGreen" x1="0" y1="0" x2="1" y2="0">
        <stop offset="0" stop-color="#23772f"/>
        <stop offset=".6" stop-color="#3aa440"/>
        <stop offset="1" stop-color="#23772f"/>
      </linearGradient>
    </defs>
    <polygon points="0,115 280,115 300,140 300,430 0,445" fill="url(#greenBand)"/>
    <polygon points="440,0 640,0 640,340 500,460 250,205" fill="#ffe438"/>
    <g role="img" aria-label="Photo of a screened pool enclosure at dusk">
      <polygon points="450,0 640,0 640,330 505,445 265,205" fill="url(#poolScene)"/>
    </g>
    <g role="img" aria-label="Photo of workers installing an enclosure roof">
      <rect x="68" y="338" width="126" height="126" rx="10" transform="rotate(45 131 401)" fill="#5f8fb8" stroke="#ffe438" stroke-width="6"/>
    </g>
    <g role="img" aria-label="Photo of trainees reviewing plans on site">
      <rect x="258" y="259" width="186" height="186" rx="12" transform="rotate(45 351 352)" fill="#8a7a66" stroke="#ffe438" stroke-width="7"/>
    </g>
    <polygon points="0,697 225,697 330,828 0,828" fill="#ffe438"/>
    <polygon points="265,722 640,722 640,828 330,828" fill="url(#footGreen)"/>
  </svg>

  <div class="brand"><span class="brand-mark"></span><span class="brand-name">Crestview Builders</span></div>
  <div class="brand-tag">Quality outdoor living since day one</div>

  <div class="headline">
    <div class="l1">Boot Camp</div>
    <div class="l2">for people</div>
    <div class="l3"><small>looking</small> For A Career</div>
    <div class="sub">or looking to</div>
    <div class="l4">Change Careers</div>
  </div>

  <h1 class="services">We Design, Manufacture and Install<br>Custom Pool Screen Enclosures</h1>

  <div class="col left">
    <div class="item"><svg width="14" height="14" viewBox="0 0 14 14"><circle cx="7" cy="7" r="6" fill="none" stroke="#23772f" stroke-width="1.4"/><path d="M4 7l2 2 4-4" fill="none" stroke="#23772f" stroke-width="1.5"/></svg><span>We have a training program to allow Non Experienced motivated people the chance at a great career that will provide a great living for them and their family.</span></div>
    <div class="item"><svg width="14" height="14" viewBox="0 0 14 14"><circle cx="7" cy="7" r="6" fill="none" stroke="#23772f" stroke-width="1.4"/><path d="M4 7l2 2 4-4" fill="none" stroke="#23772f" stroke-width="1.5"/></svg><span>5 days of training with a guaranteed job to start the following Monday....</span></div>
  </div>
  <div class="divider"></div>
  <div class="col right">
    <div class="item"><svg width="14" height="14" viewBox="0 0 14 14"><circle cx="7" cy="7" r="6" fill="none" stroke="#23772f" stroke-width="1.4"/><path d="M4 7l2 2 4-4" fill="none" stroke="#23772f" stroke-width="1.5"/></svg><span>This is good for both someone with no construction experience or someone with construction experience that wants to upgrade their current job</span></div>
    <div class="item"><svg width="14" height="14" viewBox="0 0 14 14"><circle cx="7" cy="7" r="6" fill="none" stroke="#23772f" stroke-width="1.4"/><path d="M4 7l2 2 4-4" fill="none" stroke="#23772f" stroke-width="1.5"/></svg><span>This will be a paid boot camp, week long, we provide all the initial training for them to make a transition into our business.</span></div>
  </div>

  <div class="camp">
    <h2>Paid Boot Camp</h2>
    <div class="item"><svg width="14" height="14" viewBox="0 0 14 14"><circle cx="7" cy="7" r="6" fill="none" stroke="#23772f" stroke-width="1.4"/><path d="M4 7l2 2 4-4" fill="none" stroke="#23772f" stroke-width="1.5"/></svg><span>Transition to a full time job with great pay</span></div>
    <div class="item"><svg width="14" height="14" viewBox="0 0 14 14"><circle cx="7" cy="7" r="6" fill="none" stroke="#23772f" stroke-width="1.4"/><path d="M4 7l2 2 4-4" fill="none" stroke="#23772f" stroke-width="1.5"/></svg><span>Benefits include Health Insurance, Dental and Vision, 401K, we provide the tools and training.</span></div>
  </div>

  <div class="contact">
    <div class="row"><span class="ico"><svg width="11" height="11" viewBox="0 0 24 24"><path d="M6.6 10.8a15 15 0 006.6 6.6l2.2-2.2c.3-.3.7-.4 1-.2 1.1.4 2.3.6 3.6.6.6 0 1 .4 1 1V20c0 .6-.4 1-1 1A17 17 0 013 4c0-.6.4-1 1-1h3.5c.6 0 1 .4 1 1 0 1.3.2 2.5.6 3.6.1.3 0 .7-.2 1z" fill="#23772f"/></svg></span><span class="phone">555-014-2290</span></div>
    <div class="row"><span class="ico"><svg width="11" height="11" viewBox="0 0 24 24"><rect x="2" y="5" width="20" height="14" rx="2" fill="#23772f"/><path d="M2 6l10 7 10-7" fill="none" stroke="#ffe438" stroke-width="2"/></svg></span><span class="txt">hello@crestview-mail.com</span></div>
    <div class="row" style="align-items:flex-start"><span class="ico"><svg width="11" height="11" viewBox="0 0 24 24"><path d="M12 2a7 7 0 00-7 7c0 5 7 13 7 13s7-8 7-13a7 7 0 00-7-7zm0 9.5A2.5 2.5 0 1112 6a2.5 2.5 0 010 5.5z" fill="#23772f"/></svg></span><span class="txt">218 Harbor Lane, Sunport<br>FL 30091</span></div>
  </div>
</div>
</body>
</html>
```